you will use Ai to Copy the website Quellabyx.com to come up with the basic frame work and it will give you the understanding of how I would like Zandoprik.com to be like. Zandoprik.com is a peer to peer rv rental site very similar to both of the other rv rental sites the difference is that are commission based 20% and above per rental and we will be one flat monthly rate and they keep all the earnings. Below is photo that will help you with the color scheme and the look and feel of the design

```html
<!DOCTYPE html>
<html lang="en">
<head>
<meta charset="utf-8">
<title>Zandoprik.com – Peer-to-peer RV rentals</title>
<link href="https://fonts.googleapis.com/css2?family=Bebas+Neue&family=Inter:wght@400;500;600;700&display=swap" rel="stylesheet">
<style>
:root{
  --forest:#2f4a24;
  --forest-dark:#223818;
  --moss:#5f8a32;
  --moss-light:#7aa63e;
  --cream:#f6f4ee;
  --ink:#1f2a1a;
  --muted:#555c50;
  --white:#ffffff;
  --star:#4d7a2a;
}
*{box-sizing:border-box;margin:0;padding:0}
html,body{width:800px;height:1200px;overflow:hidden}
body{position:relative;background:var(--cream);font-family:"Inter",sans-serif;color:var(--ink)}
.abs{position:absolute}
.display{font-family:"Bebas Neue",sans-serif;letter-spacing:.5px}

/* hero */
.hero-photo{left:0;top:0;width:800px;height:380px;
  background:linear-gradient(180deg,#3d4f52 0%,#6a7a74 30%,#3f5a5e 52%,#2c3b2a 75%,#1e2a1b 100%)}
.hero-photo::after{content:"";position:absolute;inset:0;background:linear-gradient(90deg,rgba(15,25,12,.75) 0%,rgba(15,25,12,.35) 45%,rgba(0,0,0,0) 70%)}
.logo{left:24px;top:20px;color:var(--white);font-weight:700;font-size:28px;letter-spacing:-.5px}
.nav{top:20px;left:343px;font-size:9px;font-weight:600;color:var(--white)}
.nav a{color:inherit;text-decoration:none}
.nav .link{position:absolute;top:3px;white-space:nowrap}
.btn-signup{left:710px;top:15px;width:65px;height:25px;background:var(--moss);color:var(--white);font-size:9.5px;font-weight:600;display:flex;align-items:center;justify-content:center;border-radius:3px}
.headline{left:31px;top:100px;font-size:50px;line-height:42px;color:var(--white)}
.headline .accent{color:var(--moss-light)}
.headline-rule{left:33px;top:230px;width:262px;height:2px;background:rgba(255,255,255,.85)}
.hero-copy{left:33px;top:244px;width:280px;font-size:11px;line-height:16px;color:var(--white)}
.btn{display:flex;align-items:center;justify-content:center;font-size:10.5px;font-weight:500;border-radius:3px;color:var(--white)}
.btn-primary{background:var(--moss)}
.btn-list{left:33px;top:288px;width:101px;height:26px}
.btn-browse{left:144px;top:288px;width:100px;height:26px;border:1px solid var(--white)}

/* search */
.search-panel{left:84px;top:319px;width:634px;height:86px;background:var(--forest);border-radius:6px}
.search-box{left:96px;top:331px;width:611px;height:42px;background:var(--white);border-radius:4px}
.field{position:absolute;top:0;height:42px;display:flex;align-items:center;gap:10px}
.field-label{font-size:7px;color:var(--muted)}
.field-value{font-size:8.5px;color:var(--ink);margin-top:3px}
.field-sep{position:absolute;top:8px;width:1px;height:26px;background:#d8d8d0}
.btn-search{position:absolute;right:8px;top:8px;width:95px;height:26px;background:var(--forest-dark);color:var(--white);font-size:9px;font-weight:600;border-radius:3px;display:flex;align-items:center;justify-content:center}
.trust-line{left:84px;top:382px;width:634px;display:flex;justify-content:center;align-items:center;gap:6px;font-size:9px;color:var(--white)}

/* features */
.feature{top:426px;display:flex;gap:9px;align-items:flex-start}
.feature-icon{width:39px;height:39px;border-radius:50%;background:var(--forest);display:flex;align-items:center;justify-content:center;flex-shrink:0}
.feature-icon.light{background:var(--moss)}
.feature h3{font-size:8px;font-weight:700;letter-spacing:.3px;margin-top:6px}
.feature p{font-size:7px;line-height:11px;color:var(--muted);margin-top:3px}
.feature-sep{top:428px;width:1px;height:40px;background:#d6d4c8}

/* browse */
.section-title{font-size:21px;color:var(--forest)}
.view-all{left:686px;top:504px;font-size:8.5px;font-weight:600;color:var(--forest)}
.card{top:527px;width:162px;height:152px;background:var(--white);border-radius:4px;box-shadow:0 1px 4px rgba(0,0,0,.15);overflow:hidden}
.card-photo{height:97px;position:relative}
.card-fav{position:absolute;right:7px;top:7px}
.card-body{padding:8px 7px 0 8px}
.card-name{font-size:8px;font-weight:600}
.card-meta{font-size:6.5px;color:var(--muted);margin-top:5px}
.card-foot{display:flex;justify-content:space-between;align-items:baseline;margin-top:6px}
.rating{font-size:6.5px;color:var(--muted)}
.rating b{color:var(--star)}
.price{font-size:10.5px;font-weight:700}
.price small{font-size:6.5px;font-weight:400;color:var(--muted)}
.arrow-btn{top:574px;width:22px;height:22px;border-radius:50%;background:var(--white);box-shadow:0 1px 3px rgba(0,0,0,.2);display:flex;align-items:center;justify-content:center}

/* how it works */
.how-title{left:0;top:695px;width:800px;text-align:center;font-size:20px;color:var(--forest-dark)}
.how-title span{color:var(--moss)}
.step{top:716px;width:150px;text-align:center}
.step-icon{width:42px;height:42px;margin:0 auto;border-radius:50%;background:var(--forest);border:3px solid var(--cream);box-shadow:0 0 0 1px #cfd6c4;display:flex;align-items:center;justify-content:center}
.step-icon.light{background:var(--moss)}
.step h4{font-size:8px;font-weight:700;margin-top:9px}
.step p{font-size:7px;line-height:11px;color:var(--muted);margin-top:3px}
.dash{top:739px;width:108px;border-top:1px dashed var(--moss)}

/* owners */
.owner-panel{left:58px;top:810px;width:688px;height:185px;background:var(--forest);border-radius:4px}
.owner-photo{left:69px;top:817px;width:356px;height:168px;background:linear-gradient(180deg,#7f95a2 0%,#a6b0a8 35%,#4c6a6e 55%,#3c4a2c 78%,#5b5238 100%)}
.owner-text{left:453px;top:821px;color:var(--white)}
.owner-kicker{font-size:9px;font-weight:600}
.owner-title{font-size:15.5px;font-weight:700;line-height:16px;margin-top:3px}
.owner-copy{font-size:8px;line-height:11.5px;margin-top:4px;width:200px}
.checks{list-style:none;margin-top:4px}
.checks li{display:flex;align-items:center;gap:6px;font-size:7.5px;height:12.2px}
.btn-owner{left:453px;top:967px;width:92px;height:19px;font-size:8.5px}
.learn-more{left:558px;top:971px;font-size:8.5px;color:var(--white);text-decoration:underline}

/* testimonials */
.testi-title{left:0;top:1002px;width:800px;text-align:center;font-size:11.5px;font-weight:700;color:var(--forest-dark)}
.testi{top:1022px;width:187px;height:87px;background:rgba(255,255,255,.7);border-radius:4px}
.testi .quote{position:absolute;left:12px;top:6px;font-size:16px;font-weight:700;color:var(--forest)}
.stars{position:absolute;left:43px;top:8px;font-size:9px;color:var(--star);letter-spacing:1px}
.testi p{position:absolute;left:43px;top:22px;width:137px;font-size:7px;line-height:10.5px}
.person{position:absolute;left:12px;top:57px;display:flex;gap:7px;align-items:center}
.avatar{width:26px;height:26px;border-radius:50%;background:#c9b8a3}
.person b{font-size:8px;display:block;line-height:11px}
.person span{font-size:6.5px;color:var(--muted);display:block;line-height:9px}
.dots{left:378px;top:1110px;display:flex;gap:8px}
.dots i{width:5px;height:5px;border-radius:50%;background:#9aa190}
.dots i.on{background:var(--forest)}

/* footer */
.footer{left:0;top:1121px;width:800px;height:79px;background:var(--forest-dark)}
.footer-logo{left:40px;top:1134px;font-weight:700;font-size:16px;color:var(--white)}
.footer-blurb{left:41px;top:1160px;font-size:6.5px;line-height:9.5px;width:140px;color:var(--white)}
.socials{left:41px;top:1182px;display:flex;gap:8px}
.socials i{width:9px;height:9px;border-radius:50%;background:var(--white)}
.fcol{top:1133px;color:var(--white)}
.fcol h5{font-size:6.5px;font-weight:700;letter-spacing:.3px}
.fcol li{list-style:none;font-size:6.3px;line-height:9.8px}
.fcol ul{margin-top:3px}
.footer-photo{left:662px;top:1130px;width:130px;height:66px;background:linear-gradient(135deg,#4a5a3a,#8c8f80 60%,#3b4a2c);opacity:.75;border-radius:3px}
.copyright{left:0;top:1190px;width:800px;text-align:center;font-size:6px;color:var(--white)}
</style>
</head>
<body>

<div class="abs hero-photo" role="img" aria-label="Motorhome driving a winding lakeside road beneath forested mountains"></div>
<div class="abs logo">Zandoprik.com</div>
<nav class="abs nav">
  <a class="link" style="left:0">How It Works</a>
  <a class="link" style="left:78px">List Your RV</a>
  <a class="link" style="left:155px">Browse RVs</a>
  <a class="link" style="left:230px">Resources ⌄</a>
  <a class="link" style="left:318px">Log In</a>
</nav>
<div class="abs btn-signup">Sign Up</div>

<h1 class="abs display headline">THE EASIER WAY<br><span class="accent">TO RENT &amp; EARN</span><br>WITH YOUR RV</h1>
<div class="abs headline-rule"></div>
<p class="abs hero-copy">List your RV, rent it out, and keep more of what you earn. It's simple, secure, and stress-free.</p>
<div class="abs btn btn-primary btn-list">List Your RV</div>
<div class="abs btn btn-browse">Browse RVs</div>

<div class="abs search-panel"></div>
<div class="abs search-box">
  <div class="field" style="left:18px">
  <svg width="14" height="16" viewBox="0 0 14 16" fill="none" stroke="#333" stroke-width="1.3"><path d="M7 15s5-5 5-9A5 5 0 0 0 2 6c0 4 5 9 5 9z"/><circle cx="7" cy="6" r="1.8"/></svg>
  <div><div class="field-label">Pick up location</div><div class="field-value">Enter location</div></div></div>
  <div class="field-sep" style="left:175px"></div>
  <div class="field" style="left:192px">
  <svg width="16" height="16" viewBox="0 0 16 16" fill="none" stroke="#333" stroke-width="1.3"><rect x="1.5" y="3" width="13" height="11.5" rx="1"/><path d="M1.5 6.5h13M5 1.5v3M11 1.5v3M4.5 9h1.5M7.5 9H9M10.5 9H12M4.5 11.5h1.5M7.5 11.5H9"/></svg>
  <div><div class="field-label">Pick up date</div><div class="field-value">Add dates</div></div></div>
  <div class="field-sep" style="left:340px"></div>
  <div class="field" style="left:355px">
  <svg width="15" height="15" viewBox="0 0 15 15" fill="none" stroke="#333" stroke-width="1.3"><circle cx="7.5" cy="4.5" r="3"/><path d="M1.5 14c0-3.5 2.7-5.5 6-5.5s6 2 6 5.5"/></svg>
  <div><div class="field-label">Guests</div><div class="field-value">Add guests</div></div></div>
  <div class="btn-search">Search RVs</div>
</div>
<div class="abs trust-line">
  <svg width="11" height="12" viewBox="0 0 11 12" fill="none" stroke="#fff" stroke-width="1.1"><path d="M5.5 1 10 2.7V6c0 2.7-2 4.4-4.5 5C3 10.4 1 8.7 1 6V2.7z"/><path d="m3.5 6 1.5 1.5 2.5-3"/></svg>
  Safe. Secure. Insured. Book with confidence.
</div>

<div class="abs feature" style="left:53px"><div class="feature-icon light"><svg width="22" height="18" viewBox="0 0 22 18" fill="none" stroke="#fff" stroke-width="1.4"><circle cx="11" cy="5" r="3"/><circle cx="4.5" cy="7" r="2.2"/><circle cx="17.5" cy="7" r="2.2"/><path d="M5.5 16c0-3 2.5-5 5.5-5s5.5 2 5.5 5M1 15c0-2 1.5-3.5 3.5-3.5M21 15c0-2-1.5-3.5-3.5-3.5"/></svg></div>
  <div><h3>THOUSANDS OF RVS</h3><p>Find the perfect RV<br>for your next adventure.</p></div></div>
<div class="abs feature-sep" style="left:215px"></div>
<div class="abs feature" style="left:237px"><div class="feature-icon"><svg width="18" height="20" viewBox="0 0 18 20" fill="none" stroke="#fff" stroke-width="1.4"><path d="M9 1.5 16 4v5c0 4.5-3 7.5-7 9-4-1.5-7-4.5-7-9V4z"/><path d="m5.5 10 2.5 2.5 4.5-5"/></svg></div>
  <div><h3>SECURE &amp; INSURED</h3><p>Every booking is protected<br>from start to finish.</p></div></div>
<div class="abs feature-sep" style="left:398px"></div>
<div class="abs feature" style="left:419px"><div class="feature-icon"><svg width="22" height="18" viewBox="0 0 22 18" fill="none" stroke="#fff" stroke-width="1.4"><circle cx="7" cy="5" r="2.8"/><circle cx="15" cy="5" r="2.8"/><path d="M1.5 16c0-3 2.5-5 5.5-5s5.5 2 5.5 5M10 12c1.2-.7 3-1 5-1 3 0 5.5 2 5.5 5"/></svg></div>
  <div><h3>COMMUNITY DRIVEN</h3><p>We connect RV owners<br>and travelers like you.</p></div></div>
<div class="abs feature-sep" style="left:581px"></div>
<div class="abs feature" style="left:603px"><div class="feature-icon"><svg width="22" height="22" viewBox="0 0 22 22" fill="none" stroke="#fff" stroke-width="1.4"><circle cx="11" cy="11" r="9"/><path d="M14 7.5c-.6-.8-1.7-1.3-3-1.3-1.8 0-3 .9-3 2.3 0 3 6 1.6 6 4.7 0 1.4-1.3 2.4-3 2.4-1.4 0-2.6-.6-3.2-1.5M11 4.5v2M11 15.5v2"/></svg></div>
  <div><h3>SAVE MORE</h3><p>Lower fees. Higher earnings.<br>Better for everyone.</p></div></div>

<h2 class="abs display section-title" style="left:58px;top:497px">BROWSE RVS</h2>
<div class="abs view-all">View all RVs →</div>
<div class="abs arrow-btn" style="left:19px"><svg width="8" height="10" viewBox="0 0 8 10"><path d="M6 1 2 5l4 4" fill="none" stroke="#222" stroke-width="1.5"/></svg></div>
<div class="abs arrow-btn" style="left:760px"><svg width="8" height="10" viewBox="0 0 8 10"><path d="m2 1 4 4-4 4" fill="none" stroke="#222" stroke-width="1.5"/></svg></div>

<div class="abs card" style="left:56px">
  <div class="card-photo" role="img" aria-label="Travel trailer parked among pine trees" style="background:linear-gradient(180deg,#5d7150,#a9aba0 55%,#4f5b3e)">
    <svg class="card-fav" width="13" height="12" viewBox="0 0 13 12"><path d="M6.5 11 1.5 6a3 3 0 0 1 5-3.5A3 3 0 0 1 11.5 6z" fill="none" stroke="#fff" stroke-width="1.3"/></svg></div>
  <div class="card-body"><div class="card-name">Corvane Trailline</div><div class="card-meta">2021 • Travel Trailer • Sleeps 6</div>
  <div class="card-foot"><span class="rating"><b>★</b> 4.9 (126)</span><span class="price">$89 <small>/ night</small></span></div></div>
</div>
<div class="abs card" style="left:231px">
  <div class="card-photo" role="img" aria-label="Class C motorhome on a grassy field" style="background:linear-gradient(180deg,#7d8f9c,#b2aa95 55%,#5e6b44)">
    <svg class="card-fav" width="13" height="12" viewBox="0 0 13 12"><path d="M6.5 11 1.5 6a3 3 0 0 1 5-3.5A3 3 0 0 1 11.5 6z" fill="none" stroke="#fff" stroke-width="1.3"/></svg></div>
  <div class="card-body"><div class="card-name">Halvik Roamer Elite</div><div class="card-meta">2020 • Class C • Sleeps 6</div>
  <div class="card-foot"><span class="rating"><b>★</b> 4.8 (98)</span><span class="price">$119 <small>/ night</small></span></div></div>
</div>
<div class="abs card" style="left:408px">
  <div class="card-photo" role="img" aria-label="Travel trailer in a mountain meadow" style="background:linear-gradient(180deg,#8496a0,#a8aaa2 55%,#56663f)">
    <svg class="card-fav" width="13" height="12" viewBox="0 0 13 12"><path d="M6.5 11 1.5 6a3 3 0 0 1 5-3.5A3 3 0 0 1 11.5 6z" fill="none" stroke="#fff" stroke-width="1.3"/></svg></div>
  <div class="card-body"><div class="card-name">Pemberlo Mini</div><div class="card-meta">2022 • Travel Trailer • Sleeps 5</div>
  <div class="card-foot"><span class="rating"><b>★</b> 5.0 (72)</span><span class="price">$95 <small>/ night</small></span></div></div>
</div>
<div class="abs card" style="left:582px">
  <div class="card-photo" role="img" aria-label="Class C motorhome parked on a forest road" style="background:linear-gradient(180deg,#66786a,#b6b8b0 55%,#6a6a5a)">
    <svg class="card-fav" width="13" height="12" viewBox="0 0 13 12"><path d="M6.5 11 1.5 6a3 3 0 0 1 5-3.5A3 3 0 0 1 11.5 6z" fill="none" stroke="#fff" stroke-width="1.3"/></svg></div>
  <div class="card-body"><div class="card-name">Brookvale Suncrest</div><div class="card-meta">2019 • Class C • Sleeps 7</div>
  <div class="card-foot"><span class="rating"><b>★</b> 4.7 (54)</span><span class="price">$109 <small>/ night</small></span></div></div>
</div>

<h2 class="abs display how-title">HOW <span>ZANDOPRIK.COM</span> WORKS</h2>
<div class="abs step" style="left:92px"><div class="step-icon"><svg width="20" height="20" viewBox="0 0 20 20" fill="none" stroke="#fff" stroke-width="1.8"><circle cx="8.5" cy="8.5" r="5.5"/><path d="m13 13 5 5"/></svg></div>
  <h4>1. FIND YOUR RV</h4><p>Search thousands of RVs<br>near you and book online.</p></div>
<div class="abs dash" style="left:217px"></div>
<div class="abs step" style="left:323px"><div class="step-icon light"><svg width="18" height="18" viewBox="0 0 18 18" fill="none" stroke="#fff" stroke-width="1.5"><rect x="2" y="3.5" width="14" height="12.5" rx="1"/><path d="M2 7h14M6 1.5v3.5M12 1.5v3.5M5 10h2M8.5 10h2M12 10h1.5M5 13h2M8.5 13h2"/></svg></div>
  <h4>2. HIT THE ROAD</h4><p>Pick up your RV and enjoy<br>your adventure.</p></div>
<div class="abs dash" style="left:471px"></div>
<div class="abs step" style="left:548px"><div class="step-icon"><svg width="22" height="22" viewBox="0 0 22 22" fill="none" stroke="#fff" stroke-width="1.5"><circle cx="11" cy="11" r="9"/><path d="M14 7.5c-.6-.8-1.7-1.3-3-1.3-1.8 0-3 .9-3 2.3 0 3 6 1.6 6 4.7 0 1.4-1.3 2.4-3 2.4-1.4 0-2.6-.6-3.2-1.5M11 4.5v2M11 15.5v2"/></svg></div>
  <h4>3. LEAVE A REVIEW</h4><p>Return the RV and share your<br>experience.</p></div>

<div class="abs owner-panel"></div>
<div class="abs owner-photo" role="img" aria-label="Motorhome parked at a lakeside campsite with chairs around a campfire"></div>
<div class="abs owner-text">
  <div class="owner-kicker">OWN AN RV?</div>
  <div class="owner-title">EARN MORE WITH<br>ZANDOPRIK.COM</div>
  <p class="owner-copy">List your RV and keep more of what you earn. Our low, flat monthly rate means no surprises—just more in your pocket.</p>
  <ul class="checks">
    <li><svg width="9" height="9" viewBox="0 0 9 9" fill="none" stroke="#fff" stroke-width=".9"><circle cx="4.5" cy="4.5" r="3.9"/><path d="m2.7 4.6 1.2 1.2 2.3-2.4"/></svg>Keep all your earnings</li>
    <li><svg width="9" height="9" viewBox="0 0 9 9" fill="none" stroke="#fff" stroke-width=".9"><circle cx="4.5" cy="4.5" r="3.9"/><path d="m2.7 4.6 1.2 1.2 2.3-2.4"/></svg>Low, flat monthly rate</li>
    <li><svg width="9" height="9" viewBox="0 0 9 9" fill="none" stroke="#fff" stroke-width=".9"><circle cx="4.5" cy="4.5" r="3.9"/><path d="m2.7 4.6 1.2 1.2 2.3-2.4"/></svg>24/7 support</li>
    <li><svg width="9" height="9" viewBox="0 0 9 9" fill="none" stroke="#fff" stroke-width=".9"><circle cx="4.5" cy="4.5" r="3.9"/><path d="m2.7 4.6 1.2 1.2 2.3-2.4"/></svg>Secure payments</li>
  </ul>
</div>
<div class="abs btn btn-primary btn-owner">List Your RV</div>
<div class="abs learn-more">Learn More →</div>

<h2 class="abs testi-title">WHAT OUR COMMUNITY SAYS</h2>
<div class="abs testi" style="left:93px"><span class="quote">“</span><span class="stars">★★★★★</span>
  <p>Zandoprik made our family trip unforgettable. The RV was perfect and the process was so easy!</p>
  <div class="person"><div class="avatar"></div><div><b>Dana R.</b><span>Renter</span></div></div></div>
<div class="abs testi" style="left:302px"><span class="quote">“</span><span class="stars">★★★★★</span>
  <p>As an owner, I love how much I earn compared to other platforms. Highly recommend!</p>
  <div class="person"><div class="avatar" style="background:#b59c82"></div><div><b>Owen K.</b><span>RV Owner</span></div></div></div>
<div class="abs testi" style="left:516px"><span class="quote">“</span><span class="stars">★★★★★</span>
  <p style="top:26px">Great experience from start to finish. The support team is amazing!</p>
  <div class="person"><div class="avatar" style="background:#d2b89c"></div><div><b>Clara V.</b><span>Renter</span></div></div></div>
<div class="abs dots"><i></i><i class="on"></i><i></i></div>

<footer class="abs footer"></footer>
<div class="abs footer-photo" role="img" aria-label="Motorhome parked among pine trees"></div>
<div class="abs footer-logo">Zandoprik.com</div>
<p class="abs footer-blurb">The peer-to-peer RV rental marketplace that puts owners and travelers first.</p>
<div class="abs socials"><i></i><i></i><i></i></div>
<div class="abs fcol" style="left:220px"><h5>EXPLORE</h5><ul><li>Browse RVs</li><li>How It Works</li><li>Why Zandoprik</li><li>FAQs</li></ul></div>
<div class="abs fcol" style="left:341px"><h5>FOR OWNERS</h5><ul><li>List Your RV</li><li>Owner Resources</li><li>Pricing</li><li>Success Stories</li></ul></div>
<div class="abs fcol" style="left:458px"><h5>SUPPORT</h5><ul><li>Help Center</li><li>Contact Us</li><li>Insurance</li><li>Trust &amp; Safety</li></ul></div>
<div class="abs fcol" style="left:568px"><h5>COMPANY</h5><ul><li>About Us</li><li>Careers</li><li>Blog</li><li>Terms &amp; Privacy</li></ul></div>
<div class="abs copyright">© 2025 Zandoprik.com. All rights reserved.</div>

</body>
</html>
```